Etiketten für Honig
Wir können es nicht in Worte fassen wie dankbar wir sind mit unserem Einzigartigen Design was uns Wenda die Designerin entworfen hat und unserem schönen spitzen Logo - einfach einmalig. Haben bei beiden Projekten wo Wenda mitgewirkt hat Sie als Gewinnerin ???? gekrönt Umsetzung - Geschmack - Talent Sie setzt alles so schnell um - unkompliziert und denkt selber mit, in allen Punkten wo man selber übersieht Wenda ist sehr zu empfehlen der nach etwas besonders auf der Suche ist. Danke Wenda mehr als Danke ????
Aufgabenstellung
Hallo Ihr lieben
Produktetiketten
Vorderseite
-Markenlogo ist derzeit auch bei Entwurfsplatz in Bearbeitung - mit einem Preisgeld
TERAMILO Spain
-100% Artisan Naturbelassen
Honig aus Andalusien
Sortenamen - zuerst auf Deutsch dann spanisch noch
100% Origen España
Sehr wichtig
Miel de Flores
- Berg Honig
- Miel de Monte -
- Eucalyptus Honig
- Miel de eucalipto
- Thymian Honig
- Miel Tomillo
- KastanienHonig
- Miel de castaño
- Orangenblütenhonig
- Miel azahar
Rosmarin Honig
- Miel Romero
AvocadoHonig
- Miel de Aguacate
Blütenpollen
- Bee Pollen - siehe Beispiel - Fotos
Das ist für den Mix:
Orangenblütenhonig
mit Blüten-Pollen, Gelée Royal &Propolis
Siehe Foto
Der Avocado Honig ist sehr sehr dunkel
Wenn Folie dann so das es sehr betont wird wie bei Vexa-Rino
Wenn Blüten verwendet wird denkt daran
Es sind Die Blüten von wo die Honigsorten - Geschmack entsteht
Rückseite
Abfülldatum /verfalldatum
Wird mit einer stanze drauf gemacht
Freilassen
Herkunft und Anschrift
✅100% Purer Andalusischer Honig
✅Garantiert ohne chemie
✅Abfüllung& Verpackung bei niedrigen Temperaturen & erhaltene Nährstoffe
✅ungefiltert
✅Winter nicht zugefüttert
Honig gilt als Rohkost und ist daher für Kleinkinder unter 12 Monate ungeeignet
Naturbelassener Honig kann im Laufe der Zeit kristallisieren und bei max. 40° C im Wasserbad wieder verflüssigt werden.
Wir hatten an einer no Label Ettiket gedacht
Bedeutet durchsichtige Folie
Siegelverschluss müsste dann an der Seite sein in Papierform
Die LOSnummer und ablaufdatum da drauf gestanzt werden
Könnt es bei Klebwerk.de ansehen
Und Anhang Fotos
Oder auch Baumwolle Papier da kann es i..

```html
<!DOCTYPE html>
<html lang="de">
<head>
<meta charset="utf-8">
<title>Rückseitenetikett – Honig</title>
<link href="https://fonts.googleapis.com/css2?family=Oswald:wght@400;500&family=Sacramento&display=swap" rel="stylesheet">
<style>
  :root {
    --page-bg: #e6e6e6;
    --honey-deep: #c84a06;
    --honey-mid: #dc6e0a;
    --honey-light: #ea9a2a;
    --label-ink: #ffffff;
  }
  html, body {
    margin: 0;
    padding: 0;
    width: 1200px;
    height: 800px;
    overflow: hidden;
    background: var(--page-bg);
  }
  .canvas {
    position: relative;
    width: 1200px;
    height: 800px;
  }
  .back-label {
    position: absolute;
    left: 150px;
    top: 120px;
    width: 900px;
    height: 560px;
    background: linear-gradient(135deg, var(--honey-deep) 0%, var(--honey-mid) 50%, var(--honey-light) 100%);
    color: var(--label-ink);
    font-family: "Oswald", "Arial Narrow", sans-serif;
    font-weight: 400;
    text-transform: uppercase;
    letter-spacing: 0.04em;
  }
  .variety-name {
    position: absolute;
    top: 22px;
    left: 0;
    right: 0;
    text-align: center;
    font-size: 11px;
    letter-spacing: 0.12em;
    opacity: 0.85;
  }
  .date-field {
    position: absolute;
    left: 64px;
    top: 92px;
    font-size: 17px;
    font-weight: 500;
  }
  .origin-note {
    position: absolute;
    right: 60px;
    top: 80px;
    font-family: "Sacramento", cursive;
    text-transform: none;
    letter-spacing: 0;
    font-size: 30px;
    padding-bottom: 2px;
    border-bottom: 2px solid var(--label-ink);
  }
  .quality-list {
    position: absolute;
    left: 64px;
    top: 190px;
    margin: 0;
    padding: 0;
    list-style: none;
    font-size: 16px;
    line-height: 1.55;
  }
  .notice {
    position: absolute;
    left: 64px;
    margin: 0;
    font-size: 16px;
    line-height: 1.55;
    max-width: 780px;
  }
  .notice--infants { top: 370px; }
  .notice--crystallise { top: 428px; max-width: 640px; }
</style>
</head>
<body>
<main class="canvas">
  <section class="back-label" aria-label="Rückseitenetikett Honig">
    <div class="variety-name">Miel Tomillo</div>
    <div class="date-field">Abfülldatum /Verfalldatum</div>
    <div class="origin-note">100% Origen España</div>
    <ul class="quality-list">
      <li>100% purer andalusischer Honig</li>
      <li>Garantiert ohne Chemie</li>
      <li>Abfüllung &amp; Verpackung bei niedrigen Temperaturen &amp; erhaltene Nährstoffe</li>
      <li>Ungefiltert</li>
      <li>Winter nicht zugefüttert</li>
    </ul>
    <p class="notice notice--infants">Honig gilt als Rohkost und ist daher für Kleinkinder unter 12 Monate ungeeignet</p>
    <p class="notice notice--crystallise">Naturbelassener Honig kann im Laufe der Zeit kristallisieren und bei max. 40° C im Wasserbad wieder verflüssigt werden.</p>
  </section>
</main>
</body>
</html>
```